Clinical psychologist - Psychotherapist business card

Hi everyone, I'm a clinical psychologist and psychotherapist, and I’m looking for a logo for my business card. The front will feature only the logo, while the back will include my contact details (and possibly a subtle touch of the logo). I've found two logos that I like, but the first one feels a bit childish—it lacks professionalism and doesn’t stand out from other similar designs. The second one, which I do like, unfortunately gives off a clinical, impersonal vibe.

Feel free to improvise—you don’t need to base the design on the logos I previously mentioned.

I generally prefer minimalistic designs that convey warmth, trust, and professionalism. I’d also like the card to have a bright background to make it feel inviting.

Additionally, I’m leaning toward using letterpress for the print technique, so the design should be compatible with that style—elegant, tactile, and clean. However, I’m still open to other options if they better suit the design.

UPDATE: I'm considering naming my business “Kalydo” (top-level domain: .gr), so you could incorporate that as well.

Target Market(s)

Psychology clients, Psychiatrists, Social media users

Industry/Entity Type

Clinical psychologist - Psychotherapist

Contact Information for Business Card

To be added later on

Colors

Designer to choose colors to be used in the design.

Requirements
Nice to have
• Possibly my initials on the front side. They are Δ Μ (capital letters) or δ μ (small letters).
Should not have
• Portraits of famous psychologists

```html
<!DOCTYPE html>
<html lang="en">
<head>
<meta charset="utf-8">
<title>Kalydo business card</title>
<link rel="stylesheet" href="https://fonts.googleapis.com/css2?family=Poppins:wght@300;400;500;600;800&display=swap">
<style>
  :root {
    --stage: #d6d6d6;
    --paper: #ffffff;
    --brand-red: #c1202f;
    --brand-olive: #7a5f25;
    --ink: #1d1d1d;
    --watermark: #f0ede6;
    --foil: #f1dcc4;
  }
  * { box-sizing: border-box; margin: 0; padding: 0; }
  html, body { width: 1200px; height: 711px; overflow: hidden; }
  body {
    background: var(--stage);
    font-family: "Poppins", sans-serif;
    position: relative;
  }
  .card {
    position: absolute;
    top: 198px;
    width: 550px;
    height: 314px;
    overflow: hidden;
    box-shadow: 0 6px 18px rgba(0,0,0,.18);
  }
  .card--details { left: 35px; background: var(--paper); }
  .card--brand { left: 615px; background: var(--brand-red); }

  .brand-mark {
    position: absolute;
    left: 34px; top: 30px;
    display: flex; align-items: center; gap: 10px;
    font-weight: 800;
    font-size: 40px;
    letter-spacing: 1px;
    color: var(--brand-olive);
  }
  .brand-mark__dot {
    width: 16px; height: 16px; border-radius: 50%;
    background: var(--brand-red);
  }
  .head-watermark {
    position: absolute;
    right: -10px; bottom: -40px;
    width: 300px; height: 300px;
    background: var(--watermark);
    border-radius: 46% 50% 30% 40%;
  }
  .person {
    position: absolute; left: 34px; top: 110px;
  }
  .person__name { font-size: 26px; line-height: 1.1; }
  .person__first { color: var(--brand-red); font-weight: 600; }
  .person__last { color: var(--brand-olive); font-weight: 300; }
  .person__role { font-size: 12px; font-weight: 500; color: var(--ink); margin-top: 2px; }
  .address {
    position: absolute; left: 34px; top: 172px;
    font-size: 12px; line-height: 1.45; color: var(--ink);
    font-style: normal;
  }
  .contact {
    position: absolute; left: 34px; top: 220px;
    list-style: none; font-size: 12.5px; color: var(--ink);
  }
  .contact li { display: flex; align-items: center; gap: 8px; line-height: 1.7; }
  .contact svg { width: 12px; height: 12px; fill: var(--brand-red); flex: none; }
  .contact .spacer { width: 12px; }

  .brand-foil {
    position: absolute; inset: 0;
    display: flex; align-items: center; justify-content: center; gap: 14px;
    font-weight: 800; font-size: 64px; letter-spacing: 2px;
    color: var(--foil);
  }
  .brand-foil__dot {
    width: 24px; height: 24px; border-radius: 50%;
    background: var(--foil);
  }
</style>
</head>
<body>
  <section class="card card--details">
    <div class="head-watermark" role="img" aria-label="Faint head silhouette with neuron illustration"></div>
    <div class="brand-mark"><span class="brand-mark__dot"></span>Kalydo.gr</div>
    <div class="person">
      <p class="person__name"><span class="person__first">Mara</span> <span class="person__last">Delos</span></p>
      <p class="person__role">Founder &amp; CEO</p>
    </div>
    <address class="address">418 Linden Ave. Suite 12<br>Larkfield, OR 97401</address>
    <ul class="contact">
      <li><svg viewBox="0 0 24 24"><path d="M6.6 10.8a15 15 0 0 0 6.6 6.6l2.2-2.2a1 1 0 0 1 1-.25 11.4 11.4 0 0 0 3.6.57 1 1 0 0 1 1 1V20a1 1 0 0 1-1 1A17 17 0 0 1 3 4a1 1 0 0 1 1-1h3.5a1 1 0 0 1 1 1c0 1.25.2 2.45.57 3.6a1 1 0 0 1-.25 1z"/></svg>(541) 555-0186</li>
      <li><svg viewBox="0 0 24 24"><path d="M2 5h20v14H2z M2 5l10 8 10-8" fill="none" stroke="#c1202f" stroke-width="2.4"/></svg>hello@kalydo.gr</li>
      <li><svg viewBox="0 0 24 24"><circle cx="12" cy="12" r="9" fill="none" stroke="#c1202f" stroke-width="2.4"/><path d="M3 12h18M12 3c3 3 3 15 0 18M12 3c-3 3-3 15 0 18" fill="none" stroke="#c1202f" stroke-width="2"/></svg>www.kalydo.gr</li>
    </ul>
  </section>

  <section class="card card--brand">
    <div class="brand-foil"><span class="brand-foil__dot"></span>Kalydo.gr</div>
  </section>
</body>
</html>
```